Internet and T.V. Services

We will need a two page brochure highlighting the services of satelitte t.v. and internet for our sales team. We are a camp and catering company focused on remote locations in northern Canada that would like to offer a first class t.v. and internet services to the camps that we provide catering to.

Target Market(s)

Adults based in western speaking countries aged 25-35 business professionals.

Industry/Entity Type

Internet

Font styles to use
Serif

Colors

Designer to choose colors to be used in the design.

Requirements
Must have
• -Company logo
-Two pages (4 sides)
-An emotional connection between family life and remote camp life
-Break down of services for t.v. and internet
-Pictures in background representing the above
-emphasis that it is an upsell for our company
Nice to have
• -company logo to look like a globe with an airplane flying around it (latitude and longitude lines)

```html
<!DOCTYPE html>
<html lang="en">
<head>
<meta charset="utf-8">
<title>Satellite T.V. and Internet Services</title>
<link href="https://fonts.googleapis.com/css2?family=Tinos:ital,wght@0,400;0,700;1,400&display=swap" rel="stylesheet">
<style>
  :root {
    --lime: #a9d13c;
    --gold: #f6b71b;
    --red: #b3343c;
    --blue: #1b6fae;
    --ink: #1f1f1f;
    --paper: #ffffff;
  }
  * { box-sizing: border-box; margin: 0; padding: 0; }
  html, body { width: 1200px; height: 740px; overflow: hidden; background: var(--paper); }
  body { position: relative; font-family: "Tinos", "Times New Roman", serif; color: var(--ink); }

  .page-title {
    position: absolute; top: 37px; height: 41px; background: var(--lime);
    display: flex; align-items: center; justify-content: center;
    font-weight: 700; font-size: 19px; letter-spacing: 0.3px; color: #1b1b1b;
  }
  .page-title--tv { left: 0; width: 510px; }
  .page-title--net { left: 693px; width: 507px; }

  .tv-question {
    position: absolute; left: 53px; top: 102px; width: 500px;
    color: var(--red); font-weight: 700; font-size: 18px; line-height: 22px;
  }

  .plan-box {
    position: absolute; left: 53px; top: 148px; width: 497px; height: 150px;
    background: var(--gold); padding: 9px;
  }
  .plan-box__inner {
    width: 100%; height: 100%; border: 1px dashed rgba(255,255,255,0.85);
    display: flex; padding: 12px 0 0 21px;
  }
  .plan { font-size: 13.5px; line-height: 17px; }
  .plan--short { width: 264px; }
  .plan__name { color: var(--red); font-weight: 700; font-size: 13px; margin-bottom: 9px; }
  .plan__or { color: var(--red); font-size: 8px; line-height: 10px; }

  .licensing {
    position: absolute; left: 53px; top: 313px; width: 497px; text-align: center;
    color: var(--blue); font-weight: 700; font-size: 14.5px; line-height: 18px;
  }

  .photo { position: absolute; }
  .photo--dishes {
    left: 53px; top: 380px; width: 497px; height: 188px;
    background: linear-gradient(180deg, #9aa48e 0%, #5f7550 35%, #3f5a30 70%, #2f4a22 100%);
  }
  .photo--reader {
    left: 622px; top: 90px; width: 530px; height: 353px;
    background: linear-gradient(135deg, #e9e6dd 0%, #cfc8b8 40%, #2a8c8a 65%, #b98a5e 100%);
  }

  .upgrade {
    position: absolute; left: 130px; top: 588px; display: flex; align-items: center; gap: 27px;
    font-size: 20px;
  }
  .upgrade strong { color: var(--red); }

  .rig-note {
    position: absolute; left: 53px; top: 632px; width: 520px;
    font-style: italic; font-size: 12.5px; line-height: 17px;
  }

  .net-intro {
    position: absolute; left: 622px; top: 447px; width: 545px;
    color: var(--blue); font-weight: 700; font-size: 14.5px; line-height: 18px;
  }

  .service { position: absolute; left: 622px; width: 540px; }
  .service--office { top: 502px; }
  .service--camp { top: 583px; }
  .service__name {
    color: var(--red); font-weight: 700; font-variant: small-caps; font-size: 14px;
    line-height: 17px; margin-bottom: 5px;
  }
  .service__list { list-style: none; font-size: 14px; line-height: 22.5px; }
  .service__list li::before { content: "\2756"; color: var(--red); margin-right: 5px; }
</style>
</head>
<body>

  <header class="page-title page-title--tv">SATELLITE T.V.</header>
  <header class="page-title page-title--net">INTERNET</header>

  <p class="tv-question">Is 16 channels good enough? Or do you want better? Why settle for less when you can get more?</p>

  <section class="plan-box">
    <div class="plan-box__inner">
      <div class="plan plan--short">
        <h3 class="plan__name">T.V. SHORT TERM</h3>
        <p>18 channel</p>
        <p>1 SD receiver (c/w 1 - KFN per month)</p>
        <p class="plan__or">OR</p>
        <p>36 channel</p>
        <p>1 HD receiver (c/w 1 - KFN per month)</p>
      </div>
      <div class="plan plan--long">
        <h3 class="plan__name">T.V. LONG TERM</h3>
        <p>48 channel</p>
        <p>Minimum - 1 year term</p>
        <p>1 HD receiver (c/w KFN)</p>
        <p class="plan__or">OR</p>
        <p>60 channels</p>
      </div>
    </div>
  </section>

  <p class="licensing">Minimum - 3 year term - due to licensing<br>1 Electronic Programming Guide + 3 In House Channels<br>2 - HD Receivers (both come with KFN)</p>

  <div class="photo photo--dishes" role="img" aria-label="Satellite dishes on a forested mountain slope"></div>

  <div class="upgrade">
    <svg width="60" height="26" viewBox="0 0 60 26" aria-hidden="true">
      <path d="M2 9 H40 V2 L58 13 L40 24 V17 H2 Z" fill="#b3343c"/>
    </svg>
    <span>Time for an <strong>UPGRADE?</strong></span>
  </div>

  <p class="rig-note">****Rig Camps will come with Fully Loaded Receivers including The Summit Channel as well as Free KFN on the TV in the Recreation room.</p>

  <div class="photo photo--reader" role="img" aria-label="Woman relaxing on a bed using a laptop beside an open book"></div>

  <p class="net-intro">Are you feeling disconnected from the outside world? Our ‘better’ internet brings you into the moments you may miss while you’re away.</p>

  <section class="service service--office">
    <h3 class="service__name">Satellite Internet - Office System</h3>
    <ul class="service__list">
      <li>Single Modem Internet Service (4 to 6 users) - Hardwire preferred</li>
      <li>VOIP phone line (Edmonton area code)</li>
    </ul>
  </section>

  <section class="service service--camp">
    <h3 class="service__name">Camp/Dorm System</h3>
    <ul class="service__list">
      <li>Dual Modem Internet Service (20 to 30 users)</li>
      <li>PC Server controlled load sharing/cache interface</li>
      <li>Wireless Radios</li>
    </ul>
  </section>

</body>
</html>
```